30th birthday flyer

I would like a flyer made up for my 30th birthday.
The event will be held on boat, and cruise the river
Theme on flyer nautical, Boat party,
Vessel is : MV TORVELLA
Flyer must include:

Friday 06th April 5:00PM to 8:30PM
418 Kelbrook Terrace, Noosaville, QLD
Food and Booze provided

```html
<!DOCTYPE html>
<html lang="en">
<head>
<meta charset="utf-8">
<title>30th Birthday Boat Party Flyer</title>
<link href="https://fonts.googleapis.com/css2?family=Lato:ital,wght@0,700;1,900&family=Kaushan+Script&display=swap" rel="stylesheet">
<style>
  :root {
    --backdrop: #3a3a3c;
    --paper: #ffffff;
    --ink: #2b2b2b;
    --pink: #e6157d;
    --purple: #8e2f91;
    --purple-light: #a84aa8;
    --purple-dark: #6e1f74;
    --ball: #8a3cb4;
    --ball-light: #c98ad8;
    --ball-dark: #5e2288;
    --banner: #0c0c0c;
    --banner-edge: #c8201f;
  }
  * { margin: 0; padding: 0; box-sizing: border-box; }
  html, body { width: 924px; height: 1200px; overflow: hidden; background: var(--backdrop); }
  .canvas { position: relative; width: 924px; height: 1200px; background: var(--backdrop); }

  .flyer {
    position: absolute; left: 100px; top: 88px; width: 724px; height: 1024px;
    background: radial-gradient(ellipse at 50% 45%, var(--paper) 72%, #e6e6e6 100%);
    overflow: hidden;
  }

  .host-photo {
    position: absolute; left: 0; top: 0; width: 348px; height: 424px;
    background: linear-gradient(180deg, #f1eeec 0%, #e2c3b5 30%, #e8a7ae 62%, #f0b9c0 100%);
    border-bottom-right-radius: 60px;
  }

  .star-burst {
    position: absolute; left: 300px; top: 60px; width: 424px; height: 380px;
    border-radius: 46% 0 0 40%;
    background: linear-gradient(150deg, #fbd3bd 0%, #f6c02a 35%, #3fa6e0 62%, #ee72b8 100%);
  }

  .confetti-band {
    position: absolute; left: 0; top: 392px; width: 560px; height: 64px;
    border-radius: 0 30px 0 0;
    background: linear-gradient(90deg, #e8401f 0%, #f39a1c 40%, #f4c51a 70%, #3b7fd0 100%);
  }

  .dot-band {
    position: absolute; left: 0; top: 612px; width: 480px; height: 80px;
    border-radius: 0 0 80px 0;
    background: linear-gradient(90deg, #1a1a1a 0%, #5a5a5a 45%, #8cc04a 100%);
    opacity: .85;
  }

  .paint-splash {
    position: absolute; left: 440px; top: 600px; width: 284px; height: 300px;
    border-radius: 30% 0 40% 60%;
    background: linear-gradient(180deg, #9b45b8 0%, #d873c0 55%, #f06a3a 100%);
  }

  .disco-ball {
    position: absolute; left: 448px; top: 342px; width: 276px; height: 276px;
    border-radius: 50%;
    background: radial-gradient(circle at 48% 42%, var(--ball-light) 0%, var(--ball) 45%, var(--ball-dark) 100%);
  }

  .title-banner {
    position: absolute; left: 4px; top: 440px; width: 484px; height: 172px;
    background: var(--banner); border-radius: 22px;
    box-shadow: -4px 4px 0 var(--banner-edge);
  }
  .title-age {
    position: absolute; left: 108px; top: 6px;
    font: 400 34px/1 "Kaushan Script", cursive; color: var(--pink);
  }
  .title-word {
    position: absolute; left: 44px; top: 30px;
    font: 400 106px/1.1 "Kaushan Script", cursive; color: var(--paper);
    letter-spacing: -1px;
  }

  .event-info {
    position: absolute; left: 76px; top: 746px;
    font: 700 28.5px/32px "Lato", sans-serif; color: var(--ink);
  }
  .event-vessel {
    margin-top: 5px;
    font: italic 900 28.5px/32px "Lato", sans-serif; color: var(--pink);
    letter-spacing: -0.5px;
  }

  .details-band {
    position: absolute; left: 0; bottom: 0; width: 724px; height: 152px;
    background: radial-gradient(ellipse at 50% 40%, var(--purple-light) 40%, var(--purple) 75%, var(--purple-dark) 100%);
    padding: 22px 0 0 76px;
  }
  .details-list { list-style: none; }
  .details-list li {
    display: flex; align-items: center; gap: 11px;
    font: 700 28.5px/34.5px "Lato", sans-serif; color: var(--ink);
  }
  .details-list svg { flex: none; }
</style>
</head>
<body>
<div class="canvas">
  <div class="flyer">
    <div class="star-burst" role="img" aria-label="Party illustration of shooting stars, streamers and coloured halftone dots"></div>
    <div class="paint-splash" role="img" aria-label="Purple paint drips and pink splashes below the disco ball"></div>
    <div class="confetti-band" role="img" aria-label="Colourful confetti shards behind the title banner"></div>
    <div class="dot-band" role="img" aria-label="Black and green halftone dots under the title banner"></div>
    <div class="host-photo" role="img" aria-label="Photo of the birthday host in a captain's hat and floral shirt"></div>
    <div class="disco-ball" role="img" aria-label="Purple mirrored disco ball"></div>

    <div class="title-banner">
      <span class="title-age">30th</span>
      <span class="title-word">Birthday.</span>
    </div>

    <div class="event-info">
      <p>Event will be held on boat,<br>and cruise the river</p>
      <p class="event-vessel">Vessel is : MV TORVELLA</p>
    </div>

    <div class="details-band">
      <ul class="details-list">
        <li><svg width="19" height="21" viewBox="0 0 18 20"><path d="M0 0 L18 10 L0 20 Z" fill="#2b2b2b"/></svg>Friday 06th April 5:00PM to 8:30PM</li>
        <li><svg width="19" height="21" viewBox="0 0 18 20"><path d="M0 0 L18 10 L0 20 Z" fill="#2b2b2b"/></svg>418 Kelbrook Terrace, Noosaville, QLD</li>
        <li><svg width="19" height="21" viewBox="0 0 18 20"><path d="M0 0 L18 10 L0 20 Z" fill="#2b2b2b"/></svg>Food and Booze provided</li>
      </ul>
    </div>
  </div>
</div>
</body>
</html>
```